Meridian Clearsound Wellness LLC Card Design

Need business card with a logo for a hearing aid sales and audiology business. We have two Hearing Instrument Specialists and one Audiologist on staff. Over 25 years in business. Locally owned and operated. Financing available. Most insurances accepted.

Meridian Clearsound Wellness LLC
48730 W Larkfield, Suite 9
Spokane, WA 99371
509-617-2084
www.meridianclearsound-example.com

Manager
Tobias Wrenfield HIS COHC
License #81957260

Target Market(s)

50yr old + people with a hearing loss.

Industry/Entity Type

Business

Contact Information for Business Card

48730 W Larkfield, Suite 9
Spokane, WA 99371
509-617-2084
www.meridianclearsound-example.com

Manager
Tobias Wrenfield HIS COHC
RTEQ #81957260

Font styles to use
Serif
Sans Serif

Requirements
Must have
• Business name, Tobias's name and title(s) and contact information, License #, web address
Nice to have
Should not have

```html
<!DOCTYPE html>
<html lang="en">
<head>
<meta charset="utf-8">
<title>Meridian Clearsound Wellness LLC — Business Card</title>
<link rel="stylesheet" href="https://fonts.googleapis.com/css2?family=Lato:wght@400;700;900&display=swap">
<style>
  :root {
    --stage: #3b3c3e;
    --brand-blue: #1f63cf;
    --brand-blue-light: #2f86e6;
    --ink-blue: #2a63b8;
    --text-grey: #5a6b82;
    --rule-grey: #c9ced6;
    --accent-green: #4cb848;
    --paper: #ffffff;
  }
  * { box-sizing: border-box; margin: 0; padding: 0; }
  html, body {
    width: 1200px; height: 672px; overflow: hidden;
    background: var(--stage);
    font-family: "Lato", Arial, sans-serif;
  }
  .stage {
    width: 1200px; height: 672px;
    display: flex; align-items: center; justify-content: center; gap: 60px;
  }
  .card {
    position: relative;
    width: 525px; height: 300px;
    border-radius: 4px;
    overflow: hidden;
    box-shadow: 0 14px 30px rgba(0,0,0,0.45);
  }

  /* Front */
  .card-front {
    background: linear-gradient(135deg, var(--brand-blue) 0%, var(--brand-blue-light) 100%);
  }
  .card-front .brand {
    position: absolute; left: 48px; top: 98px;
    display: flex; align-items: center; gap: 12px;
  }
  .brand-dot {
    width: 22px; height: 22px; border-radius: 50%;
    background: rgba(255,255,255,0.9);
    flex: none;
  }
  .brand-name {
    font-weight: 900; font-size: 19px; letter-spacing: 1.5px;
    text-transform: uppercase; line-height: 1.15;
    max-width: 260px;
  }
  .card-front .brand-name { color: #ffffff; }
  .front-mark {
    position: absolute; right: 48px; top: 34px;
    width: 130px; height: 130px; border-radius: 50%;
    background: rgba(255,255,255,0.12);
  }

  /* Back */
  .card-back { background: var(--paper); }
  .card-back .brand {
    position: absolute; left: 34px; top: 36px;
    display: flex; align-items: center; gap: 12px;
  }
  .card-back .brand-dot { background: var(--accent-green); }
  .card-back .brand-name { color: var(--ink-blue); font-size: 18px; max-width: 300px; }

  .contact {
    position: absolute; left: 34px; top: 150px; width: 400px;
  }
  .person-name {
    color: var(--ink-blue); font-size: 17px; font-weight: 700;
    padding-bottom: 8px; border-bottom: 1px solid var(--rule-grey);
  }
  .person-title { font-weight: 400; font-size: 12px; }
  .details {
    margin-top: 8px; color: var(--text-grey);
    font-size: 11.5px; line-height: 1.6;
  }
  .details-rule {
    margin-top: 14px; width: 330px; height: 1px;
    background: var(--rule-grey); margin-left: 60px;
  }
  .bottom-band {
    position: absolute; left: 0; right: 0; bottom: 0; height: 7px;
    display: flex;
  }
  .band-blue { flex: 0 0 72%; background: var(--brand-blue); }
  .band-green { flex: 1; background: var(--accent-green); }
</style>
</head>
<body>
  <main class="stage">
    <section class="card card-front" aria-label="Card front">
      <div class="brand">
        <span class="brand-dot"></span>
        <span class="brand-name">Meridian Clearsound Wellness LLC</span>
      </div>
      <div class="front-mark"></div>
    </section>

    <section class="card card-back" aria-label="Card back">
      <div class="brand">
        <span class="brand-dot"></span>
        <span class="brand-name">Meridian Clearsound Wellness LLC</span>
      </div>
      <div class="contact">
        <p class="person-name">Tobias Wrenfield, <span class="person-title">HIS, COHC</span></p>
        <p class="details">
          RTEQ #81957260 &nbsp;|&nbsp; 509 617 2084 &nbsp;|&nbsp; www.meridianclearsound-example.com<br>
          48730 W Larkfield, Suite 9 Spokane, WA 99371
        </p>
        <div class="details-rule"></div>
      </div>
      <div class="bottom-band">
        <span class="band-blue"></span>
        <span class="band-green"></span>
      </div>
    </section>
  </main>
</body>
</html>
```